Rock band business card design

I need an edgy double sided business card to hand out at music events and to send out to radio.

It needs to display our logo, web address and social media icons (plazzo, chirpex, sonicvaultly).

Colour scheme to match our website (www.torvelkash.com)

Please include this quote:
Bright embers rising... a stirring... TORVEL KASH.

Logo files have been attached.

I look forward to seeing your designs!

Target Market(s)

radio stations, music fans.

Industry/Entity Type

Events

Requirements
Must have
• Website address, social media icons, quote, colour scheme to match www.torvelkash.com

```html
<!DOCTYPE html>
<html lang="en">
<head>
<meta charset="utf-8">
<title>Torvel Kash – Business Card</title>
<link rel="stylesheet" href="https://fonts.googleapis.com/css2?family=Tinos:wght@400;700&display=swap">
<style>
  :root {
    --stage: #2b2b2b;
    --cream: #f4e8d2;
    --peach: #efc08f;
    --sage: #c9c7a2;
    --ink: #1c1a17;
    --sand-light: #f2c77a;
    --sand-mid: #c99a55;
    --sand-dark: #7d5a30;
  }
  * { margin: 0; padding: 0; box-sizing: border-box; }
  html, body {
    width: 1200px; height: 900px; overflow: hidden;
    background: var(--stage);
    font-family: "Tinos", "Times New Roman", serif;
  }
  .stage {
    width: 1200px; height: 900px;
    display: flex; flex-direction: column; align-items: center; justify-content: center;
    gap: 40px;
  }
  .card {
    width: 700px; height: 400px; display: block;
    box-shadow: 0 10px 30px rgba(0,0,0,.45);
  }
  .card text { font-family: "Tinos", "Times New Roman", serif; fill: var(--ink); }
  .brand-name { font-size: 30px; letter-spacing: 1px; }
  .quote { font-size: 22px; font-weight: 700; }
  .quote-name { font-size: 25px; font-weight: 700; letter-spacing: 1px; }
  .web { font-size: 15px; font-weight: 700; }
  .social { font-size: 14px; font-weight: 700; }
  .front-name { font-size: 56px; letter-spacing: 2px; }
</style>
</head>
<body>
<main class="stage">

  <!-- Information side -->
  <svg class="card card-back" viewBox="0 0 700 400" xmlns="http://www.w3.org/2000/svg">
    <rect class="card-base" width="700" height="400" fill="var(--cream)"/>
    <rect class="band-top" width="700" height="30" fill="var(--peach)"/>
    <path class="tab-top" d="M430 68 Q440 44 466 44 H700 V82 H430 Z" fill="var(--sage)"/>

    <text class="brand-name" x="40" y="62">TORVEL KASH</text>
    <rect class="brand-mark" x="50" y="76" width="130" height="130" fill="var(--ink)" role="img" aria-label="Torvel Kash band mark"/>

    <text class="quote" x="250" y="150">Bright embers rising... a stirring...</text>
    <text class="quote-name" x="470" y="190" text-anchor="middle">TORVEL KASH.</text>

    <rect class="band-line" y="212" width="700" height="16" fill="var(--peach)"/>
    <rect class="band-main" y="228" width="700" height="92" fill="var(--sage)"/>
    <text class="web" x="30" y="256">www.torvelkash.com</text>

    <g class="socials">
      <rect x="240" y="288" width="12" height="12" fill="var(--ink)"/>
      <text class="social" x="258" y="299">plazzo</text>
      <rect x="380" y="288" width="12" height="12" fill="var(--ink)"/>
      <text class="social" x="398" y="299">chirpex</text>
      <rect x="520" y="288" width="12" height="12" fill="var(--ink)"/>
      <text class="social" x="538" y="299">sonicvaultly</text>
    </g>

    <rect class="band-line" y="320" width="700" height="22" fill="var(--peach)"/>
    <rect class="band-bottom" y="342" width="700" height="58" fill="var(--sage)"/>
  </svg>

  <!-- Photo side -->
  <svg class="card card-front" viewBox="0 0 700 400" xmlns="http://www.w3.org/2000/svg">
    <defs>
      <linearGradient id="desertSky" x1="0" y1="0" x2="1" y2="1">
        <stop offset="0" stop-color="var(--sand-mid)"/>
        <stop offset="0.5" stop-color="var(--sand-dark)"/>
        <stop offset="1" stop-color="var(--sand-light)"/>
      </linearGradient>
    </defs>
    <rect class="photo" width="700" height="400" fill="url(#desertSky)" role="img" aria-label="Photograph of ancient stone pyramids against a golden sunset sky"/>
    <rect class="stripe-left" y="245" width="160" height="32" fill="var(--sage)"/>
    <path class="banner" d="M0 277 H150 Q160 250 188 250 H520 Q548 250 556 280 V400 H0 Z" fill="var(--peach)"/>
    <rect class="stripe-right" x="556" y="330" width="144" height="46" fill="var(--sage)"/>
    <text class="front-name" x="278" y="352" text-anchor="middle">TORVEL KASH</text>
  </svg>

</main>
</body>
</html>
```